A5 Certificate for a running Brisora Challenge

I would like a certificate designed called the "Brisora 50K Running Challenge"

It is presented to people that have run 50k in Mallorca across 10 runs. So they have to run 10 runs with a minimum distance of 5K per run. This gives a total of 50k.

The certificate will need:

1. Map of Mallorca in the background
2. Picture of a runner
3. Main title at the front to say "Brisora 50k Running Challenge"
4. Space to put the runners name on it. "Awarded to:"
5. Space to put the date the certificate is awarded. "Date Awarded:"

The design is then up to you but it needs to look official and professional. It is designed for teenagers so it needs to be "cool" and bold.

Any questions please ask.

Target Market(s)

Teenagers who want something cool and bold.

Font styles to use
Sans Serif

Colors
0556a4
fbee3f
33a6d7

Requirements
Must have
• 1. Map of Mallorca in the background
• 2. Picture of a runner
• 3. Main title at the front to say "Brisora 50k Running Challenge"
• 4. Space to put the runners name on it. "Awarded to:"
• 5. Space to put the date the certificate is awarded. "Date Awarded:"
Nice to have
• Mallorca is a sunny holiday location so it would be good to have sea blue colours and the sun in the design. to show the running challenge was done on a holiday island.

```html
<!DOCTYPE html>
<html lang="en">
<head>
<meta charset="utf-8">
<title>Brisora 50K Running Challenge Certificate</title>
<link rel="stylesheet" href="https://fonts.googleapis.com/css2?family=Libre+Baskerville:wght@400;700&family=Dancing+Script:wght@500&display=swap">
<style>
  :root {
    --sun-light: #fbe46a;
    --sun-deep: #f6c53f;
    --sea-light: #33a6d7;
    --sea-deep: #0556a4;
    --card-frame: #5bb8e6;
    --card-top: #ffffff;
    --card-bottom: #e6e9ef;
    --island: #f8ef8c;
    --island-soft: rgba(248, 239, 140, 0);
    --runner: #f7941d;
    --medal: #f7a823;
    --medal-core: #e1b24a;
    --ink: #14305a;
    --rule: #3c4a63;
  }
  html, body {
    margin: 0;
    padding: 0;
    width: 1200px;
    height: 848px;
    overflow: hidden;
    background: #ffffff;
  }
  .certificate {
    position: relative;
    width: 1200px;
    height: 848px;
    overflow: hidden;
    background: radial-gradient(ellipse at 50% 40%, var(--sun-light) 0%, var(--sun-light) 45%, var(--sun-deep) 100%);
  }
  .sea {
    position: absolute;
    inset: 0;
  }
  .card {
    position: absolute;
    left: 44px;
    top: 44px;
    width: 1106px;
    height: 752px;
    border: 3px solid var(--card-frame);
    background: linear-gradient(180deg, var(--card-top) 0%, var(--card-top) 55%, var(--card-bottom) 100%);
    box-sizing: border-box;
  }
  .island {
    position: absolute;
    left: 130px;
    top: 40px;
    width: 860px;
    height: 650px;
    border-radius: 50%;
    background: radial-gradient(ellipse at 55% 50%, var(--island) 0%, var(--island) 50%, var(--island-soft) 72%);
  }
  .runner {
    position: absolute;
    left: 40px;
    top: 40px;
    width: 140px;
    height: 190px;
    border-radius: 40px;
    background: linear-gradient(160deg, #f9a43c 0%, var(--runner) 100%);
  }
  .medal {
    position: absolute;
    left: 914px;
    top: 66px;
    width: 100px;
    height: 162px;
  }
  .title {
    position: absolute;
    left: 0;
    right: 0;
    top: 250px;
    margin: 0;
    text-align: center;
    font-family: "Libre Baskerville", Georgia, serif;
    font-weight: 700;
    font-size: 40px;
    letter-spacing: 0.5px;
    color: var(--ink);
  }
  .awarded-to {
    position: absolute;
    left: 0;
    right: 0;
    top: 336px;
    margin: 0;
    text-align: center;
    font-family: "Libre Baskerville", Georgia, serif;
    font-size: 17px;
    color: var(--ink);
  }
  .name-line {
    position: absolute;
    left: 186px;
    top: 434px;
    width: 734px;
    border-top: 2px dashed var(--rule);
  }
  .statement {
    position: absolute;
    left: 0;
    right: 0;
    top: 496px;
    margin: 0;
    text-align: center;
    font-family: "Libre Baskerville", Georgia, serif;
    font-weight: 700;
    font-size: 16px;
    color: var(--ink);
  }
  .sign-field {
    position: absolute;
    top: 600px;
    width: 172px;
    border-top: 2px solid var(--rule);
    text-align: center;
    font-family: "Dancing Script", cursive;
    font-size: 28px;
    color: var(--rule);
    padding-top: 4px;
  }
  .sign-field.date { left: 165px; }
  .sign-field.signature { left: 769px; }
</style>
</head>
<body>
<main class="certificate">
  <svg class="sea" width="1200" height="848" viewBox="0 0 1200 848" aria-hidden="true">
    <path d="M0 540 C260 520 520 580 760 620 C940 650 1080 640 1200 600 L1200 848 L0 848 Z" fill="var(--sea-light)"/>
    <path d="M0 560 C240 560 520 620 780 660 C960 690 1100 680 1200 650 L1200 848 L0 848 Z" fill="var(--sea-deep)"/>
    <path d="M0 760 C300 790 700 830 1200 790 L1200 848 L0 848 Z" fill="var(--sea-light)" opacity="0.6"/>
  </svg>

  <section class="card">
    <div class="island" role="img" aria-label="Map of the island in the background"></div>
    <div class="runner" role="img" aria-label="Runner in mid stride"></div>

    <div class="medal" role="img" aria-label="Award rosette">
      <svg width="100" height="162" viewBox="0 0 100 162" aria-hidden="true">
        <path d="M28 80 L18 158 L38 144 L50 160 L50 90 Z M72 80 L82 158 L62 144 L50 160 L50 90 Z" fill="var(--runner)"/>
        <circle cx="50" cy="50" r="48" fill="var(--medal)"/>
        <circle cx="50" cy="50" r="34" fill="#fff3c4"/>
        <circle cx="50" cy="50" r="26" fill="var(--medal-core)"/>
      </svg>
    </div>

    <h1 class="title">BRISORA 50K RUNNING CHALLENGE</h1>
    <p class="awarded-to">THIS CERTIFICATE IS AWARDED TO</p>
    <div class="name-line"></div>
    <p class="statement">Successfully finished the Brisora 50K Running Challenge.</p>

    <div class="sign-field date">Date Awarded</div>
    <div class="sign-field signature">Signature</div>
  </section>
</main>
</body>
</html>
```